Lone Star Wetland Flora Stewardship Guild

We need to design the home page of this new website. We would like a fun website design for provides as a resource for members and information for potential members.
Please design so that we can see a portion of background on each side on the website.
I just need the final design files psd no coding needed.
Attached is their logo (colors are not 100% set in stone either so can mess with those as I did in the quick mockup attached)
Attached is a pdf newsletter they send out, you can get a feel for them and what they are about. The design is crappy and we are here to fix that going forward and we are starting with the website.
Here are some quick example websites (design style is open)
- I attached a quick mockup i did just for a content visual but by all means do what you want.
- http://www.brindlecourtleaders.org/
- http://www.qvelto.org/
- http://preview.plimworks7.com/view.php?cat=layoutpacks&host=gridcrafthub&temp=venrolite
- http://www.ploughvale.org/
- http://www.townmarrow.org/
- http://www.projectkindlecoat.org/
here are some of the other chapters website (pretty bad!)
and here are some of the others:
- http://www.zrelkq.org/
- http://ovtu.org/
- http://www.lirvx.org/
Content Items that need to be included:
1. Logo
2. Menu - home, about, members, resources, events, membership, contact
3. Become a member - button or action
4. social links - friendwall, jobrungo, clipzora
5. banner - that needs to explain their purpose "Promoting environmental stewardship through operations, research, education and outreach" (or this can be worked into the design)
6. Upcoming event (s)
7. Advertisement - members can place an ad on the website, this can be a placeholder for now
8. newsletter signup
9. advertise with us - this link can be in the footer
30-60 years of age, succesfull (household budgets of 120K+ men and women that live in texas.
Education

```html
<!DOCTYPE html>
<html lang="en">
<head>
<meta charset="utf-8">
<title>Lone Star Wetland Flora Stewardship Guild</title>
<link href="https://fonts.googleapis.com/css2?family=Ubuntu:wght@400;500;700&display=swap" rel="stylesheet">
<style>
:root{
  --navy:#0d4a8e;
  --navy-dark:#0a3c74;
  --red:#d9495a;
  --red-band:rgba(204,64,82,.9);
  --ink:#333;
  --body:#4a4a4a;
  --footer:#231f20;
  --topbar:#3b3f4e;
  --header-bg:#f3f3f3;
}
*{margin:0;padding:0;box-sizing:border-box}
html,body{width:1200px;height:1035px;overflow:hidden}
body{font-family:"Ubuntu",sans-serif;background:linear-gradient(#e8e8e8 141px,#e6e6e6 141px,#fff 520px);position:relative;color:var(--body)}
.topbar{position:absolute;left:0;top:0;width:1200px;height:6px;background:var(--topbar)}
.header{position:absolute;left:0;top:6px;width:1200px;height:83px;background:var(--header-bg)}
.header-stripe{position:absolute;left:0;top:89px;width:1200px;height:4px;background:var(--red)}
.navband{position:absolute;left:0;top:93px;width:1200px;height:48px;background:var(--navy)}
.brand{position:absolute;left:140px;top:36px;display:flex;align-items:center;gap:8px}
.brand-dot{width:22px;height:22px;border-radius:50%;background:var(--red)}
.brand-name{font-size:44px;font-weight:700;color:var(--navy);letter-spacing:1px}
.org-title{position:absolute;left:352px;top:66px;font-size:18px;font-weight:500;color:var(--ink);text-transform:uppercase;letter-spacing:.2px}
.social-top{position:absolute;left:736px;top:19px;display:flex;gap:9.5px}
.social-top span{width:28px;height:28px;border-radius:50%;display:block}
.c-friend{background:#1a5ea8}.c-job{background:#3a9ad1}.c-rss{background:#ef8a2c}.c-clip{background:#d52a24}
.utility{position:absolute;left:894px;top:24px;display:flex;align-items:center;font-size:16px;font-weight:500;color:var(--navy)}
.utility .sep{width:1px;height:24px;background:#ccc;margin:0 6px 0 8px}
.join{position:absolute;left:891px;top:65px;width:168px;height:24px;background:var(--red);color:#fff;font-size:15.5px;text-align:center;line-height:24px;text-transform:uppercase;letter-spacing:.3px}
.nav{position:absolute;top:93px;left:398px;height:48px;display:flex;align-items:center}
.nav a{color:#fff;text-decoration:none;font-size:16px;font-weight:500;padding:0 17px;border-left:1px solid #2f69a8;line-height:34px}
.nav a:first-child{border-left:none}
.slider{position:absolute;left:141px;top:166px;width:918px;height:329px}
.slide-photo{position:absolute;left:0;top:0;width:918px;height:289px;background:linear-gradient(180deg,#e8eee6 0%,#c7d7b3 30%,#6f9a4a 55%,#8a9a5c 75%,#5c7a36 100%)}
.caption{position:absolute;left:0;top:289px;width:918px;height:37px;background:var(--red-band);color:#fff;font-size:20px;font-weight:500;text-align:center;line-height:38px}
.slider-base{position:absolute;left:0;top:326px;width:918px;height:3px;background:var(--navy)}
.arrow{position:absolute;top:142px;width:28px;height:43px;background:#f4f4f4;box-shadow:0 0 3px rgba(0,0,0,.25)}
.arrow.prev{left:-4px}.arrow.next{left:894px}
.col{position:absolute;top:524px}
.col h2{font-size:19px;font-weight:500;color:var(--ink);text-transform:uppercase;padding-left:2px;height:36px}
.rule{height:3px;border-bottom:1px solid var(--red);position:relative}
.rule i{position:absolute;left:0;top:0;height:3px;background:var(--navy)}
.about{left:141px;width:281px}
.about p{font-size:13.5px;line-height:18.5px;letter-spacing:.3px;margin:18px 2px 0}
.about p+p{margin-top:11px}
.btn{position:absolute;height:30px;background:var(--navy);color:#fff;font-size:13.5px;font-weight:500;line-height:30px;padding-left:7px;display:flex;align-items:center;gap:5px;border-radius:2px}
.events{left:460px;width:283px}
.event{display:flex;gap:13px;padding:19px 0 8px 1px;border-bottom:1px solid #ddd;height:72px}
.event:first-of-type{padding-top:20px}
.event:last-of-type{border-bottom:none}
.thumb{width:71px;height:54px;flex:none;border:1px solid #ccc}
.event .date{font-size:13.5px;font-weight:500;color:var(--navy)}
.event .desc{font-size:13.5px;line-height:16px;letter-spacing:.8px;margin-top:4px}
.ad{position:absolute;left:778px;top:529px;width:281px;height:290px}
.ad-photo{height:213px;background:linear-gradient(160deg,#2d4d6e,#18324f 60%,#0f2740)}
.ad-foot{height:77px;background:#dedede}
.footer{position:absolute;left:141px;top:847px;width:918px;height:184px;background:var(--footer);clip-path:polygon(28px 0,890px 0,918px 30px,918px 184px,0 184px,0 30px)}
.footer-line{position:absolute;left:141px;top:1031px;width:918px;height:4px;background:var(--red)}
.fcol{position:absolute;top:17px;color:#fff}
.fcol h3{font-size:16px;font-weight:500;letter-spacing:.3px}
.links{left:21px}
.links ul{list-style:none;margin-top:14px;font-size:12.5px;line-height:17.2px;font-weight:500}
.news{left:166px;width:190px}
.news p{font-size:12.5px;font-weight:500;line-height:18px;margin-top:14px}
.news .field{margin-top:9px;width:179px;height:27px;background:#fff;border-radius:2px;color:#666;font-size:12px;font-style:italic;line-height:27px;padding-left:11px}
.news .send{margin-top:13px;width:113px;height:29px;background:var(--navy);border:1px solid #9cb6d6;border-radius:2px;font-size:15px;font-weight:500;text-align:center;line-height:27px}
.follow{left:411px}
.follow ul{list-style:none;margin-top:12px}
.follow li{display:flex;align-items:center;gap:10px;height:29.5px;font-size:12.5px;font-weight:500;letter-spacing:.3px}
.follow li span{width:22px;height:22px;border-radius:50%;display:block}
.fbrand{position:absolute;left:660px;top:60px;display:flex;align-items:center;gap:10px}
.fbrand .brand-dot{width:24px;height:24px}
.fbrand .brand-name{font-size:48px;color:#fff}
</style>
</head>
<body>
<div class="topbar"></div>
<header>
  <div class="header"></div>
  <div class="header-stripe"></div>
  <div class="navband"></div>
  <div class="brand"><span class="brand-dot"></span><span class="brand-name">LSWFSG</span></div>
  <div class="org-title">Lone Star Wetland Flora Stewardship Guild</div>
  <div class="social-top" aria-label="Social links">
    <span class="c-friend" title="friendwall"></span><span class="c-job" title="jobrungo"></span><span class="c-rss" title="rss"></span><span class="c-clip" title="clipzora"></span>
  </div>
  <div class="utility">
    Contact
    <svg width="22" height="16" viewBox="0 0 22 16" style="margin-left:8px"><rect x="1" y="2" width="20" height="13" fill="#111"/><path d="M1 2 L11 10 L21 2" stroke="#fff" stroke-width="1.5" fill="none"/></svg>
    <span class="sep"></span>
    Login
    <svg width="18" height="18" viewBox="0 0 18 18" style="margin-left:10px"><circle cx="9" cy="9" r="6" fill="none" stroke="#444" stroke-width="3" stroke-dasharray="3 1.7"/><circle cx="9" cy="9" r="2.5" fill="#444"/></svg>
  </div>
  <div class="join">Become a Member</div>
  <nav class="nav">
    <a>Home</a><a>About</a><a>Members</a><a>Resources</a><a>Events</a><a>Membership</a><a>Contact</a>
  </nav>
</header>

<section class="slider">
  <div class="slide-photo" role="img" aria-label="Photo of tall reeds at the edge of a calm pond with trees beyond"></div>
  <div class="caption">Promoting Environmental Stewardship Through Operations, Research, Education And Outreach</div>
  <div class="slider-base"></div>
  <div class="arrow prev"><svg width="28" height="43" viewBox="0 0 28 43"><path d="M18 12 L10 21.5 L18 31" stroke="#222" stroke-width="3.5" fill="none"/></svg></div>
  <div class="arrow next"><svg width="28" height="43" viewBox="0 0 28 43"><path d="M10 12 L18 21.5 L10 31" stroke="#222" stroke-width="3.5" fill="none"/></svg></div>
</section>

<section class="col about">
  <h2>About LSWFSG</h2>
  <div class="rule"><i style="width:131px"></i></div>
  <p>The Lone Star Wetland Flora Stewardship Guild, Inc. is an organization of scientists, educators, students, commercial pesticide applicators, administrators, and concerned individuals interested in the management and study of aquatic plants.</p>
  <p>The membership reflects a diversity of federal, state, and local agencies; universities and colleges around the world; corporations; and small businesses.</p>
</section>
<div class="btn" style="left:141px;top:789px;width:112px">READ MORE <svg width="18" height="14" viewBox="0 0 18 14"><path d="M2 1 L8 7 L2 13 M9 1 L15 7 L9 13" stroke="#e0505f" stroke-width="2.2" fill="none"/></svg></div>

<section class="col events">
  <h2>Upcoming Events</h2>
  <div class="rule"><i style="width:174px"></i></div>
  <div class="event"><div class="thumb" role="img" aria-label="Venue logo thumbnail" style="background:#f4f4f4"></div><div><div class="date">1 AUG 2014</div><div class="desc">Lorem ipsum dolor sit amet consectetuer adipiscing</div></div></div>
  <div class="event"><div class="thumb" role="img" aria-label="Water lily pads on a pond" style="background:linear-gradient(135deg,#8a7a4a,#b7c25a,#6a6a3a)"></div><div><div class="date">2 AUG 2014</div><div class="desc">Lorem ipsum dolor sit amet consectetuer adipiscing</div></div></div>
  <div class="event"><div class="thumb" role="img" aria-label="Trees reflected in still water" style="background:linear-gradient(180deg,#dfe6e2,#5f8a3c 55%,#4a6a4a)"></div><div><div class="date">3 AUG 2014</div><div class="desc">Lorem ipsum dolor sit amet consectetuer adipiscing</div></div></div>
</section>
<div class="btn" style="left:461px;top:789px;width:94px">VIEW ALL <svg width="18" height="14" viewBox="0 0 18 14"><path d="M2 1 L8 7 L2 13 M9 1 L15 7 L9 13" stroke="#e0505f" stroke-width="2.2" fill="none"/></svg></div>

<aside class="ad" role="img" aria-label="Member advertisement: water treatment product containers">
  <div class="ad-photo"></div>
  <div class="ad-foot"></div>
</aside>

<footer class="footer">
  <div class="fcol links">
    <h3>Quick Links</h3>
    <ul><li>Home</li><li>About</li><li>Members</li><li>Resources</li><li>Events</li><li>Membership</li><li>Contact</li></ul>
  </div>
  <div class="fcol news">
    <h3>Subscribe to Newsletter</h3>
    <p>get latest updates by entering your email address</p>
    <div class="field">Email Address</div>
    <div class="send">Subscribe</div>
  </div>
  <div class="fcol follow">
    <h3>Follow Us</h3>
    <ul>
      <li><span class="c-friend"></span>Follow Us On Friendwall</li>
      <li><span class="c-job"></span>Follow Us On Jobrungo</li>
      <li><span class="c-rss"></span>Follow Us On rss</li>
      <li><span class="c-clip"></span>Follow Us On Clipzora</li>
    </ul>
  </div>
  <div class="fbrand"><span class="brand-dot"></span><span class="brand-name">LSWFSG</span></div>
</footer>
<div class="footer-line"></div>
</body>
</html>
```